new business venture [ self employed ] will register my business name as " LEARNOVA "
what I will offer is :-
computer lessons for new beginners.
Initial set up and basic overview.
lessons per hour in the comfort of your own home.
special rates for customers aged 50+
First lesson is half price with no obligation for booking any further appointments.
a learning and training plan will be presented based on your requirements.
an appraisal update on your new skills.

contact info:-
0161 4972015
07700 918342
grenwick@vellumail.net

```html
<!DOCTYPE html>
<html lang="en">
<head>
<meta charset="utf-8">
<title>Learnova – Computer Lessons Flyer</title>
<link rel="stylesheet" href="https://fonts.googleapis.com/css2?family=Bebas+Neue&family=Arimo:wght@400;700&family=Dancing+Script:wght@500&display=swap">
<style>
  :root {
    --page-bg: #e6e7e9;
    --brand-blue: #2459a8;
    --accent-blue: #2ea6e0;
    --sky-blue: #5cc2f0;
    --band-grey: #a9abae;
    --ink: #111111;
    --white: #ffffff;
    --silver-light: #f4f4f5;
    --silver-dark: #9fa1a6;
    --footer-top: #5c5d60;
    --footer-bottom: #2b2c2e;
    --logo-grey: #3b3c3f;
  }
  html, body {
    margin: 0;
    padding: 0;
    width: 1169px;
    height: 1200px;
    overflow: hidden;
    background: var(--page-bg);
  }
  .canvas {
    position: relative;
    width: 1169px;
    height: 1200px;
  }
  .flyer {
    position: absolute;
    left: 160px;
    top: 0;
    width: 848px;
    height: 1200px;
    display: block;
  }
  .title { font-family: "Bebas Neue", "Arial Narrow", sans-serif; fill: var(--white); }
  .tagline { font-family: "Dancing Script", cursive; fill: var(--white); font-size: 21px; }
  .call-heading { font-family: "Bebas Neue", "Arial Narrow", sans-serif; fill: var(--brand-blue); }
  .call-number { font-family: "Arimo", Arial, sans-serif; font-weight: 700; font-size: 19px; fill: var(--ink); }
  .section-heading { font-family: "Bebas Neue", "Arial Narrow", sans-serif; fill: var(--sky-blue); stroke: var(--white); stroke-width: 0.6px; }
  .section-script { font-family: "Dancing Script", cursive; fill: var(--white); font-size: 20px; }
  .list-text { font-family: "Arimo", Arial, sans-serif; font-size: 12.5px; fill: var(--white); }
  .footer-text { font-family: "Arimo", Arial, sans-serif; font-weight: 700; font-size: 12px; fill: var(--white); }
  .brand-name { font-family: "Arimo", Arial, sans-serif; font-weight: 700; font-size: 17px; fill: var(--logo-grey); letter-spacing: 2px; }
</style>
</head>
<body>
<main class="canvas">
  <svg class="flyer" viewBox="0 0 606 858" preserveAspectRatio="none" xmlns="http://www.w3.org/2000/svg">
    <defs>
      <linearGradient id="ribbon-silver" x1="0" y1="0" x2="1" y2="0">
        <stop offset="0" stop-color="var(--silver-dark)"/>
        <stop offset="0.35" stop-color="var(--silver-light)"/>
        <stop offset="0.7" stop-color="var(--silver-light)"/>
        <stop offset="1" stop-color="var(--silver-dark)"/>
      </linearGradient>
      <linearGradient id="photo-tones" x1="0" y1="0" x2="0" y2="1">
        <stop offset="0" stop-color="#d9c39a"/>
        <stop offset="0.4" stop-color="#c9ccd2"/>
        <stop offset="0.7" stop-color="#5d616a"/>
        <stop offset="1" stop-color="#17181b"/>
      </linearGradient>
      <linearGradient id="footer-shade" x1="0" y1="0" x2="0" y2="1">
        <stop offset="0" stop-color="var(--footer-top)"/>
        <stop offset="1" stop-color="var(--footer-bottom)"/>
      </linearGradient>
    </defs>

    <rect class="paper" x="0" y="0" width="606" height="858" fill="var(--white)"/>

    <!-- top blue header with swoosh -->
    <path class="header-swoosh-accent" d="M0 350 C200 215 420 182 606 196 V185 C430 168 220 198 0 340 Z" fill="var(--accent-blue)"/>
    <path class="header-band" d="M0 0 H606 V186 C430 170 220 200 0 341 Z" fill="var(--brand-blue)"/>

    <!-- single hero photo area, clear of ribbon and call-to-action -->
    <path class="hero-photo" role="img" aria-label="Photo of a smiling businesswoman in a dark suit holding an open laptop"
          d="M192 262 H268 V190 H606 V512 H262 V398 H192 Z" fill="url(#photo-tones)"/>

    <!-- lower swoosh bands -->
    <path class="lower-accent" d="M0 522 C170 470 400 472 606 508 V858 H0 Z" fill="var(--accent-blue)"/>
    <path class="lower-grey" d="M0 535 C170 492 410 496 606 540 V858 H0 Z" fill="var(--band-grey)"/>
    <path class="lower-band" d="M0 540 C170 505 400 512 606 575 V858 H0 Z" fill="var(--brand-blue)"/>

    <!-- ribbon with brand name -->
    <g class="brand-ribbon">
      <path d="M20 0 H177 V245 L98 212 L20 245 Z" fill="url(#ribbon-silver)"/>
      <circle cx="98" cy="90" r="32" fill="var(--brand-blue)"/>
      <text class="brand-name" x="98" y="150" text-anchor="middle">LEARNOVA</text>
    </g>

    <!-- headline -->
    <text class="title" x="385" y="86" text-anchor="middle" font-size="58" textLength="350" lengthAdjust="spacingAndGlyphs">COMPUTER LESSONS</text>
    <text class="tagline" x="385" y="120" text-anchor="middle">We've made it easy for you to gain</text>
    <text class="tagline" x="385" y="143" text-anchor="middle">new skills and learn best practices!</text>

    <!-- call to action -->
    <text class="call-heading" x="42" y="436" font-size="40" textLength="178" lengthAdjust="spacingAndGlyphs">CALL US TODAY</text>
    <g class="phone-icon" fill="var(--ink)">
      <path d="M42 452 C42 440 93 440 93 452 V457 H81 V451 H54 V457 H42 Z"/>
      <path d="M52 458 L58 452 H77 L83 458 L88 475 H47 Z"/>
      <circle cx="67.5" cy="464" r="5" fill="var(--white)"/>
    </g>
    <text class="call-number" x="97" y="457">0161 4972015</text>
    <text class="call-number" x="97" y="480">07700 918342</text>

    <!-- services -->
    <text class="section-heading" x="90" y="553" font-size="30">DISCOVER</text>
    <text class="section-script" x="92" y="575">Our Services:</text>
    <g class="services-list">
      <circle cx="46" cy="598" r="4" fill="var(--sky-blue)"/>
      <text class="list-text" x="63" y="603">Computer lessons for new beginners.</text>
      <circle cx="46" cy="630" r="4" fill="var(--sky-blue)"/>
      <text class="list-text" x="63" y="635">Initial set up and basic overview.</text>
      <circle cx="46" cy="668" r="4" fill="var(--sky-blue)"/>
      <text class="list-text" x="63" y="667">Lessons per hour in the comfort of your</text>
      <text class="list-text" x="63" y="683">own home.</text>
      <circle cx="46" cy="718" r="4" fill="var(--sky-blue)"/>
      <text class="list-text" x="63" y="714">A learning and training plan will be</text>
      <text class="list-text" x="63" y="730">presented based on your requirements.</text>
      <circle cx="46" cy="757" r="4" fill="var(--sky-blue)"/>
      <text class="list-text" x="63" y="762">An appraisal update on your new skills.</text>
    </g>

    <!-- offers -->
    <text class="section-heading" x="360" y="612" font-size="30">SEE OUR</text>
    <text class="section-script" x="362" y="642">Best offers...</text>
    <g class="offers-list">
      <path d="M349 670 L354 676 L364 663" fill="none" stroke="var(--sky-blue)" stroke-width="3" stroke-linecap="round" stroke-linejoin="round"/>
      <text class="list-text" x="368" y="676">Special rates for customers aged 50+</text>
      <path d="M349 703 L354 709 L364 696" fill="none" stroke="var(--sky-blue)" stroke-width="3" stroke-linecap="round" stroke-linejoin="round"/>
      <text class="list-text" x="368" y="709">First lesson is half price with no</text>
      <text class="list-text" x="368" y="725">obligation for booking any further</text>
      <text class="list-text" x="368" y="741">appointments.</text>
    </g>

    <!-- footer -->
    <rect class="footer-bar" x="0" y="796" width="606" height="62" fill="url(#footer-shade)"/>
    <rect class="footer-rule" x="0" y="796" width="606" height="2" fill="#8a8b8e"/>
    <g class="footer-phone-icon">
      <rect x="95" y="809" width="38" height="30" rx="7" fill="var(--accent-blue)"/>
      <path d="M101 821 C101 813 127 813 127 821 V824 H121 V820 H107 V824 H101 Z" fill="var(--white)"/>
      <path d="M106 826 L109 822 H119 L122 826 L124 834 H104 Z" fill="var(--white)"/>
      <circle cx="114" cy="829" r="2.6" fill="var(--accent-blue)"/>
    </g>
    <text class="footer-text" x="151" y="822">0161 4972015</text>
    <text class="footer-text" x="151" y="837">07700 918342</text>
    <g class="footer-mail-icon">
      <rect x="320" y="813" width="42" height="23" rx="2" fill="var(--white)"/>
      <path d="M322 815 L341 829 L360 815" fill="none" stroke="var(--accent-blue)" stroke-width="2"/>
      <rect x="321" y="814" width="40" height="21" rx="2" fill="none" stroke="var(--accent-blue)" stroke-width="1.5"/>
    </g>
    <text class="footer-text" x="369" y="829">GRENWICK@VELLUMAIL.NET</text>

    <rect x="0.5" y="0.5" width="605" height="857" fill="none" stroke="#ffffff" stroke-width="1"/>
  </svg>
</main>
</body>
</html>
```